Business Card Design Project

We need a business card to reflect the design of our website - just so it all ties in - it has a retro feel and can be found at http://www.velorasoulpair.com
We will need our phone 0437 215 964
Web address, and email velorapair@fernmail.com included
Our catch cry is "Classic Cocktail Music"
Perfect Live Music for Private & Corporate Events, Weddings and Dinner Music
Our names should be included :-
Maribel Thorne / piano & Dennis Holloway / bass
I am now also including our logo so that it can be included (in part or whole) somehow in the design
My partner thinks we should include our logo in some form in the design of the card - i will attach this here for you. I will attach eps but if you prefer another format please let me know
Regards
Mari

```html
<!DOCTYPE html>
<html lang="en">
<head>
<meta charset="utf-8">
<title>Velora Pair – Business Card</title>
<link rel="stylesheet" href="https://fonts.googleapis.com/css2?family=Poppins:wght@700;800&family=Bungee+Inline&display=swap">
<style>
  :root {
    --stage-dark: #242424;
    --stage-light: #ffffff;
    --card-white: #ffffff;
    --card-teal: #80b3b5;
    --ribbon-teal: #0b5450;
    --badge-teal: #7fb3b5;
    --icon-orange: #d9532f;
    --icon-ring: #f3c2b2;
    --ink: #111111;
    --banner-black: #161616;
    --banner-cream: #f4ecb0;
    --headline: #ffffff;
  }
  * { margin: 0; padding: 0; box-sizing: border-box; }
  html, body { width: 1200px; height: 787px; overflow: hidden; }
  body {
    position: relative;
    background: var(--stage-light);
    font-family: "Poppins", sans-serif;
    color: var(--ink);
  }
  .stage-band {
    position: absolute; left: 0; top: 0;
    width: 1200px; height: 522px;
    background: var(--stage-dark);
  }
  .card {
    position: absolute; left: 170px; top: 0;
    width: 860px; height: 510px;
    background: var(--card-teal);
    overflow: hidden;
  }
  .card__top {
    position: absolute; left: 0; top: 0;
    width: 860px; height: 205px;
    background: var(--card-white);
  }
  .card__art {
    position: absolute; left: 0; top: 0;
    width: 860px; height: 510px;
  }
  .service {
    position: absolute; top: 24px;
    width: 120px;
    text-align: center;
    text-transform: uppercase;
    font-weight: 800;
    font-size: 14.5px;
    letter-spacing: 0.4px;
  }
  .service__icon { display: block; margin: 0 auto 10px; width: 80px; height: 80px; }
  .service--weddings { left: 32px; }
  .service--packages { left: 151px; }
  .service--corporate { left: 591px; }
  .service--private { left: 704px; }

  .brand {
    position: absolute; left: 329px; top: 5px;
    width: 200px; height: 190px;
    display: flex; align-items: center; justify-content: center;
  }
  .brand__disc {
    position: absolute; left: 5px; top: 0;
    width: 190px; height: 190px;
    border-radius: 50%;
    background: var(--badge-teal);
  }
  .brand__name {
    position: relative;
    margin-top: -30px;
    font-weight: 800;
    font-size: 30px;
    line-height: 1;
    text-transform: uppercase;
    color: var(--ink);
  }
  .tagline {
    position: absolute; left: 277px; top: 163px;
    width: 304px; height: 38px;
    display: flex; align-items: center; justify-content: center;
    font-family: "Bungee Inline", sans-serif;
    font-size: 19px;
    color: var(--banner-cream);
    letter-spacing: 0.3px;
  }
  .headline {
    position: absolute; left: 130px; top: 229px;
    width: 590px;
    text-align: center;
    text-transform: uppercase;
    font-weight: 800;
    font-size: 26px;
    line-height: 35px;
    letter-spacing: 0.6px;
    color: var(--headline);
    text-shadow: 0 2px 5px rgba(0,0,0,0.45);
  }
  .contact {
    position: absolute; left: 35px; top: 408px;
    border-collapse: collapse;
    text-transform: uppercase;
    font-weight: 800;
    font-size: 14px;
  }
  .contact th { text-align: left; font-weight: 800; padding: 0 0 5px 0; width: 88px; }
  .contact td { padding: 0 0 5px 0; }
  .member {
    position: absolute; top: 410px;
    width: 200px;
    text-align: center;
    text-transform: uppercase;
    font-weight: 800;
    font-size: 18px;
    line-height: 22px;
  }
  .member__name {
    display: block;
    border-bottom: 1px solid rgba(255,255,255,0.75);
  }
  .member--piano { left: 431px; }
  .member--bass { left: 640px; }
</style>
</head>
<body>
  <div class="stage-band"></div>

  <section class="card" aria-label="Velora Pair business card">
    <div class="card__top"></div>

    <svg class="card__art" viewBox="0 0 860 510" aria-hidden="true">
      <polygon points="299,0 559,0 559,354 429,296 299,354" fill="var(--ribbon-teal)"/>
      <polygon points="232,152 300,152 300,198 232,193 246,173" fill="var(--banner-black)"/>
      <polygon points="626,152 558,152 558,198 626,193 612,173" fill="var(--banner-black)"/>
      <rect x="275" y="159" width="308" height="44" fill="var(--banner-black)"/>
      <rect x="279" y="163" width="300" height="36" fill="none" stroke="#555" stroke-width="1"/>
    </svg>

    <div class="service service--weddings">
      <svg class="service__icon" viewBox="0 0 80 80" aria-hidden="true">
        <circle cx="40" cy="40" r="39" fill="var(--icon-ring)"/>
        <circle cx="40" cy="40" r="37" fill="var(--icon-orange)"/>
        <rect x="27" y="22" width="26" height="36" rx="2" fill="none" stroke="var(--ink)" stroke-width="3"/>
        <line x1="33" y1="22" x2="33" y2="58" stroke="var(--ink)" stroke-width="2"/>
        <line x1="47" y1="22" x2="47" y2="58" stroke="var(--ink)" stroke-width="2"/>
        <line x1="33" y1="40" x2="47" y2="40" stroke="var(--ink)" stroke-width="2"/>
      </svg>
      Weddings
    </div>
    <div class="service service--packages">
      <svg class="service__icon" viewBox="0 0 80 80" aria-hidden="true">
        <circle cx="40" cy="40" r="39" fill="var(--icon-ring)"/>
        <circle cx="40" cy="40" r="37" fill="var(--icon-orange)"/>
        <path d="M40 17 a14 14 0 0 1 9 25 c-2 2 -3 5 -3 8 h-12 c0 -3 -1 -6 -3 -8 a14 14 0 0 1 9 -25z" fill="var(--ink)"/>
        <rect x="34" y="52" width="12" height="3" fill="var(--ink)"/>
        <rect x="34" y="57" width="12" height="3" fill="var(--ink)"/>
        <rect x="36" y="62" width="8" height="3" rx="1" fill="var(--ink)"/>
      </svg>
      Packages
    </div>
    <div class="service service--corporate">
      <svg class="service__icon" viewBox="0 0 80 80" aria-hidden="true">
        <circle cx="40" cy="40" r="39" fill="var(--icon-ring)"/>
        <circle cx="40" cy="40" r="37" fill="var(--icon-orange)"/>
        <rect x="16" y="30" width="14" height="10" rx="2" transform="rotate(35 23 35)" fill="var(--ink)"/>
        <rect x="50" y="30" width="14" height="10" rx="2" transform="rotate(-35 57 35)" fill="var(--ink)"/>
        <rect x="26" y="34" width="28" height="16" rx="7" fill="var(--ink)"/>
      </svg>
      Corporate
    </div>
    <div class="service service--private">
      <svg class="service__icon" viewBox="0 0 80 80" aria-hidden="true">
        <circle cx="40" cy="40" r="39" fill="var(--icon-ring)"/>
        <circle cx="40" cy="40" r="37" fill="var(--icon-orange)"/>
        <g fill="none" stroke="var(--ink)" stroke-width="3">
          <ellipse cx="40" cy="40" rx="22" ry="8"/>
          <ellipse cx="40" cy="40" rx="22" ry="8" transform="rotate(60 40 40)"/>
          <ellipse cx="40" cy="40" rx="22" ry="8" transform="rotate(-60 40 40)"/>
        </g>
        <circle cx="40" cy="40" r="4" fill="var(--ink)"/>
      </svg>
      Private
    </div>

    <div class="brand">
      <span class="brand__disc"></span>
      <span class="brand__name">Velora Pair</span>
    </div>

    <p class="tagline">Classic Cocktail Music</p>

    <h1 class="headline">Perfect live music for<br>private &amp; corporate events,<br>weddings and dinner music</h1>

    <table class="contact">
      <tr><th>Phone</th><td>0437 215 964</td></tr>
      <tr><th>Website</th><td>www.velorasoulpair.com</td></tr>
      <tr><th>Email</th><td>velorapair@fernmail.com</td></tr>
    </table>

    <p class="member member--piano"><span class="member__name">Maribel Thorne</span>Piano</p>
    <p class="member member--bass"><span class="member__name">Dennis Holloway</span>Bass</p>
  </section>
</body>
</html>
```